TLKompass online header

We need a header for our online internal company newsletter/blogsite. It is called the TLKompass which is a contraction between TLK (the department associated) and the word Gazette.
We want to have a new modern design for the header that should say "TLKompass" or "TLKompass online" (there used to be a paper version) in a nice artistic modern friendly inviting way. Sort of like a newspaper header.
There could be an optional text line that says "All the news you need" or something like that.
Target Market(s)
Consulting professionals in the area of mathematics, econometrics and IT
Industry/Entity Type
It Company
Logo Text
TLKompass
Colors
Look and feel

```html
<!DOCTYPE html>
<html lang="en">
<head>
<meta charset="utf-8">
<title>TLKompass online header</title>
<link rel="stylesheet" href="https://fonts.googleapis.com/css2?family=Fira+Sans+Extra+Condensed:wght@400;600&display=swap">
<style>
  :root {
    --backdrop: #e7e3dd;
    --paper: #ffffff;
    --ink: #111111;
    --brand-blue: #2d5f8e;
    --band-deep: #2f6ea8;
    --band-mid: #4a8ccb;
    --band-light: #9cc6ea;
    --band-edge: #235a8f;
    --visual-dark: #0d2148;
    --visual-mid: #4f86bd;
    --visual-soft: #b3bcd9;
    --visual-light: #eef0f7;
  }
  * { box-sizing: border-box; margin: 0; padding: 0; }
  html, body {
    width: 1200px;
    height: 750px;
    overflow: hidden;
    background: var(--backdrop);
    font-family: "Fira Sans Extra Condensed", "Arial Narrow", sans-serif;
  }
  .sheet {
    position: absolute;
    left: 318px;
    top: 37px;
    width: 517px;
    height: 670px;
    background: var(--paper);
    box-shadow: 0 2px 10px rgba(0,0,0,0.15);
  }
  .header-visual {
    position: absolute;
    left: 0;
    top: 0;
    width: 517px;
    height: 248px;
    background:
      linear-gradient(180deg, rgba(255,255,255,0) 60%, rgba(255,255,255,0.35) 100%),
      linear-gradient(100deg, var(--visual-dark) 0%, var(--visual-mid) 30%, var(--visual-soft) 55%, var(--visual-light) 80%, #f6f7fb 100%);
  }
  .masthead-title {
    position: absolute;
    right: 36px;
    top: 190px;
    font-size: 46px;
    font-weight: 600;
    line-height: 1;
    letter-spacing: -0.3px;
    color: var(--brand-blue);
  }
  .tagline-band {
    position: absolute;
    left: 0;
    top: 248px;
    width: 517px;
    height: 33px;
    background: linear-gradient(180deg, var(--band-light) 0 4px, var(--band-mid) 4px, var(--band-deep) 100%);
    border-bottom: 3px solid var(--band-edge);
  }
  .tagline {
    position: absolute;
    right: 30px;
    top: 7px;
    font-size: 15px;
    font-weight: 600;
    color: #ffffff;
    white-space: nowrap;
  }
  .brief {
    position: absolute;
    left: 100px;
    top: 334px;
    width: 330px;
    font-size: 18px;
    line-height: 19.5px;
    color: var(--ink);
    hyphens: manual;
  }
  .brief p + p { margin-top: 19.5px; }
</style>
</head>
<body>
  <main class="sheet">
    <div class="header-visual" role="img" aria-label="Header photograph in deep and pale blue tones"></div>
    <h1 class="masthead-title">TLKompass</h1>
    <div class="tagline-band">
      <p class="tagline">The news you need, when you need them.</p>
    </div>
    <section class="brief">
      <p>We need a header for our online internal company newsletter/blogsite. It is called the TLKompass which is a contraction between TLK (the depart&shy;ment associated) and the word Gazette.</p>
      <p>We want to have a new modern design for the header that should say "TLKompass" or "TLKompass online" (there used to be a paper version) in a nice artistic modern friendly inviting way. Sort of like a newspaper header.</p>
      <p>There could be an optional text line that says "All the news you need" or something like that.</p>
    </section>
  </main>
</body>
</html>
```